Long term design collaboration - mobile app design & web app design

We are looking for a talented mobile designer to help us improve our UI & UX for mobile app and web app.

The screens that need to be redesigned are attached.

There is potentially a lot more work in future design available for the successful candidate.
The successful candidate would have to take part in daily stand-up around 3 times per week.
The successful candidate would join a dev team
We are software company that does property management

```html
<!DOCTYPE html>
<html lang="en">
<head>
<meta charset="utf-8">
<title>Velmo – Overview</title>
<link href="https://fonts.googleapis.com/css2?family=Inter:wght@400;500;600;700&display=swap" rel="stylesheet">
<style>
:root{
  --page:#ffffff;
  --sidebar:#ffffff;
  --main:#eff2f3;
  --card:#ffffff;
  --brand:#1a14f0;
  --brand-soft:#4b47ea;
  --accent-red:#f45b6b;
  --ink:#1c1c1c;
  --muted:#6b6b6b;
  --value:#5b74c8;
  --placeholder:#8a96c8;
  --line:#e3e6ea;
  --warn:#f5b82e;
  --dark:#222222;
}
*{box-sizing:border-box;margin:0;padding:0}
html,body{width:1200px;height:1200px;overflow:hidden;background:var(--page);font-family:'Inter',sans-serif;color:var(--ink)}
.app{position:absolute;left:91px;top:116px;width:1026px;height:975px;border-radius:15px;background:var(--main);overflow:hidden;box-shadow:0 10px 60px rgba(0,0,0,.06)}
.abs{position:absolute}
.sidebar{position:absolute;left:0;top:0;width:289px;height:100%;background:var(--sidebar)}
.brand{left:64px;top:33px;font-size:30px;font-weight:600;color:var(--brand);letter-spacing:-.3px;line-height:36px}
.nav-item{position:absolute;left:19px;width:251px;height:48px;display:flex;align-items:center;padding-left:13px;gap:15px;font-size:17px;font-weight:600;border-radius:6px;color:var(--ink)}
.nav-item svg{width:18px;height:18px;flex:none}
.nav-item.active{background:var(--brand);color:#fff}
.util-item{position:absolute;left:38px;height:20px;display:flex;align-items:center;gap:12px;font-size:17px;font-weight:600}
.util-item svg{width:18px;height:18px;flex:none}
.logout{left:19px;top:889px;width:251px;height:48px;border-radius:8px;background:var(--dark);color:#fff;font-size:17px;font-weight:600;display:flex;align-items:center;justify-content:center}
.main{position:absolute;left:289px;top:0;right:0;bottom:0}
.search{left:21px;top:32px;width:450px;height:36px;border-radius:18px;background:var(--card);display:flex;align-items:center;padding-left:16px;gap:10px;font-size:12.5px;color:var(--placeholder)}
.user{right:71px;top:29px;text-align:right}
.user-name{font-size:16.5px;font-weight:600}
.user-link{font-size:13.5px;color:var(--value);margin-top:2px}
.avatar{right:19px;top:29px;width:40px;height:40px;border-radius:50%;background:linear-gradient(135deg,#8aa6a0,#c79a82)}
.h2{font-size:19px;font-weight:600;position:absolute;left:24px}
.btn{position:absolute;height:40px;width:128px;border-radius:6px;color:#fff;font-size:15px;font-weight:500;display:flex;align-items:center;justify-content:center}
.btn-primary{background:var(--brand)}
.btn-danger{background:var(--accent-red)}
.card{position:absolute;left:21px;width:697px;background:var(--card);border-radius:15px}
.setup-title{position:absolute;left:29px;top:22px;font-size:16px;font-weight:600}
.setup-row{position:absolute;left:29px;right:19px;display:flex;justify-content:space-between;align-items:center;font-size:13.5px;color:var(--muted)}
.chev{width:12px;height:12px}
.info-row{position:absolute;left:33px;right:31px;height:34px;display:flex;align-items:center;font-size:14px}
.info-row + .info-row{border-top:1px solid var(--line)}
.info-label{width:174px}
.info-value{flex:1;color:var(--value)}
.tile{position:absolute;top:721px;height:92px;border-radius:12px;background:var(--card)}
.tile-title{position:absolute;top:20px;font-size:14px;font-weight:500;display:flex;align-items:center;gap:14px}
.tile-sub{position:absolute;top:50px;font-size:10px;color:var(--value);line-height:1.3}
.tile.solid{background:var(--brand);color:#fff}
.tile.soft{background:var(--brand-soft);color:#fff}
.tile.solid .tile-sub,.tile.soft .tile-sub{color:#dfe2ff}
.ins-icon{position:absolute;left:12px;top:13px;width:48px;height:47px;border-radius:10px;background:#e6e9fb;display:flex;align-items:center;justify-content:center}
.ins-item{position:absolute;top:18px;font-size:13.5px}
.ins-item span{display:block;color:var(--value);margin-top:6px}
</style>
</head>
<body>
<div class="app">
  <aside class="sidebar">
    <div class="abs brand">Velmo</div>

    <nav>
      <div class="nav-item" style="top:114px"><svg viewBox="0 0 24 24" fill="none" stroke="#1c1c1c" stroke-width="1.8"><circle cx="12" cy="8" r="4"/><path d="M4 21c0-4 4-6 8-6s8 2 8 6z"/></svg>User Directory</div>
      <div class="nav-item" style="top:162px"><svg viewBox="0 0 24 24" fill="none" stroke="#1c1c1c" stroke-width="1.8" stroke-linecap="round" stroke-linejoin="round"><path d="M20 8H5M8 4L4 8l4 4M4 16h15M16 12l4 4-4 4"/></svg>Switch Development</div>
      <div class="nav-item" style="top:212px"><svg viewBox="0 0 24 24" fill="none" stroke="#1c1c1c" stroke-width="1.8"><path d="M6 2h9l4 4v16H6z"/><path d="M14 10h-3a1.5 1.5 0 000 3h2a1.5 1.5 0 010 3h-3M12 8.5v1.5M12 16v1.5"/></svg>Services Change</div>
      <div class="nav-item" style="top:260px"><svg viewBox="0 0 24 24" fill="none" stroke="#1c1c1c" stroke-width="1.8"><path d="M6 2h9l4 4v16H6z"/><path d="M9 11h4M9 15h7M9 18h7"/></svg>Propery Balance</div>
      <div class="nav-item active" style="top:308px"><svg viewBox="0 0 26 22" fill="none" stroke="#fff" stroke-width="1.8" stroke-linejoin="round" style="width:20px"><rect x="6" y="4" width="18" height="14" rx="1.5"/><path d="M6 5l9 7 9-7M1 9h4M2 13h3"/></svg>Sending Letter</div>
      <div class="nav-item" style="top:355px"><svg viewBox="0 0 24 24" fill="none" stroke="#1c1c1c" stroke-width="1.8"><path d="M6 2h9l4 4v16H6z"/></svg>Reguler Services</div>
      <div class="nav-item" style="top:401px"><svg viewBox="0 0 24 24" fill="none" stroke="#1c1c1c" stroke-width="1.8" stroke-linecap="round"><path d="M6 17V11a6 6 0 0112 0v6l1.5 1.5h-15z"/><path d="M10 21h4"/></svg>Notifications</div>
    </nav>

    <div class="util-item" style="top:800px"><svg viewBox="0 0 24 24" fill="none" stroke="#1c1c1c" stroke-width="1.8" stroke-linecap="round"><circle cx="12" cy="12" r="10"/><path d="M9.5 9.5a2.5 2.5 0 114 2c-1 .7-1.5 1.2-1.5 2.5M12 17.5v.1"/></svg>Support</div>
    <div class="util-item" style="top:834px"><svg viewBox="0 0 24 24" fill="none" stroke="#1c1c1c" stroke-width="1.8"><circle cx="12" cy="12" r="3"/><path d="M12 2l2 3 3.5-.8.8 3.5 3 2-2 3 .8 3.5-3.5.8-2 3-2-3-3.5-.8.8-3.5-3-2 3-2-.8-3.5 3.5.8z"/></svg>Setting</div>

    <div class="abs logout">Log out</div>
  </aside>

  <main class="main">
    <div class="abs search"><svg width="16" height="16" viewBox="0 0 24 24" fill="none" stroke="#1a14f0" stroke-width="2.2" stroke-linecap="round"><circle cx="11" cy="11" r="7"/><path d="M16.5 16.5L21 21"/></svg>Search for something</div>
    <div class="abs user"><div class="user-name">Carla Wendt</div><div class="user-link">My account</div></div>
    <div class="abs avatar" role="img" aria-label="Profile photo of the signed-in user"></div>

    <div class="h2" style="top:126px">Overview</div>
    <div class="btn btn-primary" style="left:589px;top:126px">Report</div>

    <section class="card" style="top:188px;height:182px">
      <div class="setup-title">Please complete basic setup</div>
      <div class="setup-row" style="top:59px">Service Charge Schedules<svg class="chev" viewBox="0 0 12 12" fill="none" stroke="#1a14f0" stroke-width="1.8"><path d="M2 4l4 4 4-4"/></svg></div>
      <div class="setup-row" style="top:88px">Service Charge Apportionment<svg class="chev" viewBox="0 0 12 12" fill="none" stroke="#1a14f0" stroke-width="1.8"><path d="M2 4l4 4 4-4"/></svg></div>
      <div class="setup-row" style="top:117px">Invite resident &amp; leaseholders<svg class="chev" viewBox="0 0 12 12" fill="none" stroke="#1a14f0" stroke-width="1.8"><path d="M2 4l4 4 4-4"/></svg></div>
      <div class="setup-row" style="top:146px">Connect payament provider<svg class="chev" viewBox="0 0 12 12" fill="none" stroke="#1a14f0" stroke-width="1.8"><path d="M2 4l4 4 4-4"/></svg></div>
    </section>

    <div class="btn btn-primary" style="left:21px;top:389px">Summary</div>
    <div class="btn btn-danger" style="left:172px;top:389px">Detail</div>

    <div class="h2" style="top:448px">General</div>
    <section class="card" style="top:489px;height:172px">
      <div class="info-row" style="top:14px"><div class="info-label">Unit</div><div class="info-value">85</div><svg class="chev" viewBox="0 0 12 12" fill="none" stroke="#1a14f0" stroke-width="1.8"><path d="M2 4l4 4 4-4"/></svg></div>
      <div class="info-row" style="top:48px"><div class="info-label">Handover Date</div><div class="info-value">12 Januari 2023</div><svg class="chev" viewBox="0 0 12 12" fill="none" stroke="#1a14f0" stroke-width="1.8"><path d="M2 4l4 4 4-4"/></svg></div>
      <div class="info-row" style="top:82px"><div class="info-label">Address</div><div class="info-value">24 Larkspur Row, London, W12 4QT</div><svg class="chev" viewBox="0 0 12 12" fill="none" stroke="#1a14f0" stroke-width="1.8"><path d="M2 4l4 4 4-4"/></svg></div>
      <div class="info-row" style="top:116px"><div class="info-label">Sections 20 limit</div><div class="info-value">$20</div><svg class="chev" viewBox="0 0 12 12" fill="none" stroke="#1a14f0" stroke-width="1.8"><path d="M2 4l4 4 4-4"/></svg></div>
    </section>

    <div class="h2" style="top:679px">Compliance</div>
    <div class="tile" style="left:21px;width:124px"><div class="tile-title" style="left:33px">Asbetsos</div><div class="tile-sub" style="left:35px">NA</div></div>
    <div class="tile" style="left:164px;width:145px"><div class="tile-title" style="left:25px">Legionellas<svg width="16" height="16" viewBox="0 0 24 24" fill="none" stroke="#f5b82e" stroke-width="2" stroke-linecap="round"><circle cx="12" cy="12" r="10"/><path d="M9.5 9.5a2.5 2.5 0 114 2c-1 .7-1.5 1.2-1.5 2.5M12 17.5v.1"/></svg></div><div class="tile-sub" style="left:27px">-</div></div>
    <div class="tile" style="left:328px;width:144px"><div class="tile-title" style="left:23px">Drains<svg width="16" height="16" viewBox="0 0 24 24" fill="none" stroke="#f45b6b" stroke-width="2" stroke-linecap="round" style="margin-left:28px"><circle cx="12" cy="12" r="10"/><path d="M12 7v6M12 16.5v.1"/></svg></div><div class="tile-sub" style="left:25px">Overdue<br>10 December 2023</div></div>
    <div class="tile solid" style="left:492px;width:92px"><div class="tile-title" style="left:23px">Gutters</div><div class="tile-sub" style="left:25px">NA</div></div>
    <div class="tile soft" style="left:604px;width:114px"><div class="tile-title" style="left:23px">Dry Rises</div><div class="tile-sub" style="left:25px">NA</div></div>

    <div class="h2" style="top:837px">Issurance</div>
    <section class="card" style="top:881px;height:72px">
      <div class="ins-icon"><svg width="22" height="22" viewBox="0 0 24 24" fill="none"><rect x="2" y="5" width="16" height="12" rx="2" fill="#4b6cf0"/><path d="M2 9h16" stroke="#fff" stroke-width="1.6"/><path d="M5 13h5" stroke="#fff" stroke-width="1.4"/><circle cx="18" cy="16" r="4.5" fill="#4b6cf0" stroke="#e6e9fb" stroke-width="1.4"/><path d="M18 14v4" stroke="#fff" stroke-width="1.2"/></svg></div>
      <div class="ins-item" style="left:77px">Terrorism<span>NA</span></div>
      <div class="ins-item" style="left:175px">Buildings<span>NA</span></div>
      <div class="ins-item" style="left:265px">Enggnering<span>NA</span></div>
      <div class="ins-item" style="left:388px">D &amp; O<span>NA</span></div>
      <div class="ins-item" style="left:464px">Reinstatemen<span>NA</span></div>
    </section>
  </main>
</div>
</body>
</html>
```